Tri Fold - Restaurant Brochure & pdf multipage

Develop a product guide specific to "restaurant owners" for our company's restaurant insurance services. It will need to be eye-catching, personal, unique, and industry-specific. Several Insurance flyers from our companies are attached for review. We are happy to provide guidance along the way. Our website is www.kovalenbrokerage.example. Please grab logos etc. from there. We can provide other files and more detailed copy.

Target Market(s)

Restaurant owners and CFO's

Industry/Entity Type

Insurance Broker

Font styles to use
Other font styles liked:
• match website fonts

Requirements
Must have
• WE WILL PROVIDE DETAILED CONTENT! AT THIS TIME WE ARE LOOKING FOR THE BASIC DESIGN AND LAYOUT.

EYE-CATCHING MODERN DESIGN WITH IMAGES AND BRANDED FEEL. must be print-ready and set up as a PDF to email.

brief description of our agency and its personal boutique feel specializing in the restaurant market. Also, offer a full-service solution to no only manage their business but personal risks too.

Coverages that need to be listed with a brief description: (See attached Flyers)
General Liability
FF&E (Furniture, Fixtures, and Equipment), Property
Workers Compensation
Umbrella
Liquor Liability
Auto
Cyber
Bonds
EPLI

Carrier List:
The Wexmoor
Bastion
Ferrow Common
Wayfarers
Plains Motor
Quorra
DELVA
Holloway
CountyFirst
KTO
And many more
Nice to have
• carrier logos if room.
Should not have
• TO BE DETERMINED.

```html
<!DOCTYPE html>
<html lang="en">
<head>
<meta charset="utf-8">
<title>Kovalen Brokerage – Restaurant Insurance Guide</title>
<link href="https://fonts.googleapis.com/css2?family=Playfair+Display:wght@700&family=Open+Sans:wght@400;600;700&display=swap" rel="stylesheet">
<style>
:root{
  --red:#d71f26;
  --red-dark:#a8141a;
  --ink:#111214;
  --paper:#ffffff;
  --bg:#d9dadc;
  --text:#2a2a2a;
  --carrier:#1f3b73;
}
*{box-sizing:border-box;margin:0;padding:0}
html,body{width:873px;height:1200px;overflow:hidden;background:var(--bg);font-family:"Open Sans",Arial,sans-serif;color:var(--text)}
.spread{position:relative;width:873px;height:1200px}
.page{position:absolute;top:309px;width:728px;height:1020px;background:var(--paper);transform:scale(.57);transform-origin:0 0;overflow:hidden;box-shadow:0 4px 18px rgba(0,0,0,.18)}
.page--front{left:14px}
.page--back{left:444px}
.abs{position:absolute}
.serif{font-family:"Playfair Display",Georgia,serif;font-weight:700}
.rule{display:block;width:44px;height:2px;background:var(--red);margin-top:8px}

/* front: hero */
.hero{left:0;top:0;width:728px;height:395px;background:var(--ink)}
.hero-photo{left:395px;top:18px;width:333px;height:377px;background:linear-gradient(160deg,#2e3a34 0%,#4a3a33 45%,#5a1f22 75%,#1a1c1e 100%)}
.hero-frame{left:268px;top:18px;width:130px;height:377px;border-top:2px solid #fff;border-left:2px solid #fff;border-top-left-radius:24px}
.logo-box{left:0;top:0;width:268px;height:150px;background:var(--ink);border-bottom-right-radius:30px;border-right:2px solid #fff;border-bottom:2px solid #fff}
.logo{left:34px;top:48px;display:flex;align-items:center;gap:10px}
.logo-mark{width:18px;height:18px;background:var(--red)}
.logo-name{font-family:"Playfair Display",Georgia,serif;font-weight:700;color:#fff;font-size:25px;line-height:1.05}
.headline{left:37px;top:185px;color:#fff;font-size:38px;line-height:1.08;width:360px}
.hero-copy{left:37px;top:292px;color:#fff;font-size:13.4px;line-height:1.35;width:310px;font-weight:600}
.hero-rule{left:37px;top:355px;width:72px;height:2px;background:var(--red)}

.about{left:16px;top:393px;width:696px;height:228px;background:linear-gradient(100deg,var(--red-dark),var(--red) 60%,#c5181f);border-radius:0 0 40px 40px;padding:18px 20px;color:#fff}
.about h2{font-size:23px}
.about .rule{background:#fff;opacity:.8}
.about p{font-size:8.6px;line-height:1.55;margin-top:14px}
.about p+p{margin-top:10px}

.section-title{font-size:23px;color:var(--ink)}
.mission{left:37px;top:650px;width:320px}
.mission p{font-size:8.6px;line-height:1.5;margin-top:14px}
.team{left:37px;top:758px;width:330px}
.team-grid{display:flex;gap:22px;margin-top:30px;margin-left:-8px}
.member{width:100px;text-align:center}
.portrait{width:72px;height:72px;border-radius:50%;margin:0 auto;background:radial-gradient(circle at 50% 40%,#c9a48c,#7a5a4a 60%,#4b4d52)}
.member-name{font-family:"Playfair Display",Georgia,serif;font-weight:700;color:var(--red);font-size:7px;margin-top:12px;white-space:nowrap}
.member-role{font-size:6.4px;color:#444;line-height:1.3}
.mission-photo{left:390px;top:648px;width:296px;height:262px;background:radial-gradient(circle at 55% 50%,#1f4c7a,#10233b 60%,#0a1424)}

.footer{left:16px;top:945px;width:696px;height:80px;background:var(--ink);border-radius:30px 30px 0 0;color:#fff}
.footer-addr{position:absolute;left:44px;top:12px;font-size:8.6px;line-height:1.4}
.footer-addr .place{color:var(--red);font-weight:700;font-size:9px}
.footer-phone{display:flex;align-items:center;gap:6px;font-size:17px;font-weight:700;margin-top:2px}
.footer-div{position:absolute;left:334px;top:14px;width:1px;height:44px;background:#777}
.footer-web{position:absolute;left:352px;top:20px;font-size:9.4px;line-height:2.4}
.footer-web div{display:flex;align-items:center;gap:8px}
.footer-logo{position:absolute;right:44px;top:26px;display:flex;align-items:center;gap:5px;font-family:"Playfair Display",Georgia,serif;font-weight:700;font-size:12px}
.footer-logo i{display:block;width:8px;height:8px;background:var(--red)}

/* back */
.topband{left:0;top:0;width:728px;height:20px;background:var(--ink)}
.specialties{left:16px;top:18px;width:696px;height:237px;background:linear-gradient(180deg,#202225,#0f1012);border-radius:0 0 40px 40px;color:#fff}
.specialties h2{position:absolute;left:0;right:0;top:12px;text-align:center;font-size:23px;letter-spacing:.5px}
.spec-cols{position:absolute;left:30px;top:64px;display:flex}
.spec-col{list-style:none;font-size:8.6px;font-weight:600;line-height:1.15}
.spec-col li{display:flex;gap:9px;margin-bottom:8.2px}
.spec-col li svg{flex:none;margin-top:1px}
.spec-col:nth-child(1){width:206px}
.spec-col:nth-child(2){width:240px}
.spec-col:nth-child(3){width:200px}

.policies{left:36px;top:268px;width:318px}
.policies p{font-size:8.6px;line-height:1.5;margin-top:20px;text-align:justify}
.policy-grid{display:grid;grid-template-columns:1fr 1fr;row-gap:14px;margin-top:16px}
.policy{display:flex;align-items:center;gap:9px;font-size:7.4px;font-weight:700;color:#222;line-height:1.2}
.policy-icon{flex:none;width:36px;height:36px;border:2px solid var(--red);border-radius:50%;display:flex;align-items:center;justify-content:center}
.policies-photo{left:378px;top:266px;width:328px;height:262px;background:linear-gradient(120deg,#6c7a86,#c9b7a6 45%,#2e6f79 70%,#dfe3e6)}

.coverages-frame{left:36px;top:566px;width:376px;height:196px;border:2px solid var(--ink);border-radius:22px;padding:6px}
.coverages{width:100%;height:100%;background:linear-gradient(100deg,var(--red-dark),var(--red));border-radius:16px;color:#fff;padding:16px 20px}
.coverages h2{font-size:23px}
.coverages .rule{background:#fff}
.cov-cols{display:flex;gap:22px;margin-top:10px}
.cov-cols ul{list-style:none;font-size:12.4px;line-height:1.2;color:#fff}
.cov-cols li{display:flex;gap:8px;margin-bottom:5px}
.cov-cols li::before{content:"";flex:none;width:5px;height:5px;background:#fff;margin-top:6px}

.carriers{left:434px;top:566px;width:274px}
.carrier-grid{display:grid;grid-template-columns:repeat(3,1fr);row-gap:18px;column-gap:6px;margin-top:16px}
.carrier{display:flex;align-items:center;gap:4px;font-size:8.6px;font-weight:700;color:var(--carrier);white-space:nowrap}
.carrier i{flex:none;width:7px;height:7px;background:var(--red);border-radius:50%}

.why{left:36px;top:800px;width:664px}
.why p{font-size:8.6px;line-height:1.55;margin-top:18px;text-align:justify}
</style>
</head>
<body>
<main class="spread">

  <section class="page page--front" aria-label="Restaurant insurance guide, front page">
    <div class="abs hero"></div>
    <div class="abs hero-photo" role="img" aria-label="Photo of a smiling restaurant owner in an apron standing at his restaurant entrance"></div>
    <div class="abs hero-frame"></div>
    <div class="abs logo-box">
      <div class="abs logo"><span class="logo-mark"></span><span class="logo-name">Kovalen<br>Brokerage</span></div>
    </div>
    <h1 class="abs headline serif">Restaurant Risk Advisors</h1>
    <p class="abs hero-copy">Kovalen Brokerage helps restaurant owners protect their kitchens, their teams and their future.</p>
    <span class="abs hero-rule"></span>

    <div class="abs about">
      <h2 class="serif">About Us</h2><span class="rule"></span>
      <p>Kovalen Brokerage is an independently owned boutique risk management firm with offices in Millbrook, Georgia, at Lake Ardell and thriving Downtown Fenwick, Georgia. Since 2010 we have helped countless restaurants, cafés, bars and breweries across Georgia find the right protection.</p>
      <p>Marcus Ellery started the firm because he understands what keeps owners and CFOs up at night – from a kitchen fire to a slip in the dining room. He believes in offering choices and in working for each client to give them the best possible coverage at the best possible rate, with a smooth and stress-free process.</p>
      <p>We offer a full-service solution: we manage your restaurant's business risks and your personal risks too, with plans from a multitude of A rated or better carriers.</p>
    </div>

    <div class="abs mission">
      <h2 class="section-title serif">Our Mission</h2><span class="rule"></span>
      <p><b>Our mission</b> is to give every restaurant owner a tailored risk plan at competitive prices, with the personal, boutique service a busy kitchen deserves.</p>
    </div>
    <div class="abs team">
      <h2 class="section-title serif">Our Team</h2><span class="rule"></span>
      <div class="team-grid">
        <div class="member"><div class="portrait" role="img" aria-label="Portrait of the president"></div><div class="member-name">Marcus T. Ellery, CLCS, SBCS</div><div class="member-role">President &amp; CEO</div></div>
        <div class="member"><div class="portrait" role="img" aria-label="Portrait of the office manager"></div><div class="member-name">Dana Whitlow</div><div class="member-role">Office &amp; Personal Lines<br>Account Manager</div></div>
        <div class="member"><div class="portrait" role="img" aria-label="Portrait of the commercial lines manager"></div><div class="member-name">Ines Porter, SBCS</div><div class="member-role">Commercial Lines<br>Account Manager</div></div>
      </div>
    </div>
    <div class="abs mission-photo" role="img" aria-label="Photo of two hands sheltering glowing insurance icons on a dark blue background"></div>

    <footer class="abs footer">
      <div class="footer-addr">
        <div class="place">LAKE ARDELL</div>
        <div>480 Harbor Point Lane, Suite 12, Millbrook, GA 30000</div>
        <div class="footer-phone"><svg width="10" height="12" viewBox="0 0 10 12"><path d="M2 0.5 L4 3.5 L3 4.8 Q4.3 7.6 6.4 8.9 L7.6 8 L9.8 10.2 L8.4 11.5 Q1.6 9.8 0.4 2 Z" fill="#d71f26"/></svg>(555) 014-2270</div>
      </div>
      <span class="footer-div"></span>
      <div class="footer-web">
        <div><svg width="10" height="10" viewBox="0 0 10 10"><circle cx="5" cy="5" r="4.3" fill="none" stroke="#d71f26" stroke-width="1.2"/><path d="M0.7 5H9.3M5 0.7Q2.4 5 5 9.3M5 0.7Q7.6 5 5 9.3" fill="none" stroke="#d71f26" stroke-width="0.9"/></svg>www.kovalenbrokerage.example</div>
        <div><svg width="11" height="8" viewBox="0 0 11 8"><rect x="0.5" y="0.5" width="10" height="7" fill="none" stroke="#d71f26"/><path d="M0.5 0.5 L5.5 4.5 L10.5 0.5" fill="none" stroke="#d71f26"/></svg>info@kovalenbrokerage.example</div>
      </div>
      <div class="footer-logo"><i></i>Kovalen</div>
    </footer>
  </section>

  <section class="page page--back" aria-label="Restaurant insurance guide, back page">
    <div class="abs topband"></div>
    <div class="abs specialties">
      <h2 class="serif">KOVALEN'S RESTAURANT SPECIALTIES</h2>
      <div class="spec-cols">
        <ul class="spec-col">
          <li><svg width="9" height="8" viewBox="0 0 9 8"><path d="M1 4 L3.5 6.5 L8 1" fill="none" stroke="#d71f26" stroke-width="1.6"/></svg>Full-Service Restaurants</li>
          <li><svg width="9" height="8" viewBox="0 0 9 8"><path d="M1 4 L3.5 6.5 L8 1" fill="none" stroke="#d71f26" stroke-width="1.6"/></svg>Fine Dining &amp; Chef-Owned<br>Concepts</li>
          <li><svg width="9" height="8" viewBox="0 0 9 8"><path d="M1 4 L3.5 6.5 L8 1" fill="none" stroke="#d71f26" stroke-width="1.6"/></svg>Fast Casual &amp; Quick Service</li>
          <li><svg width="9" height="8" viewBox="0 0 9 8"><path d="M1 4 L3.5 6.5 L8 1" fill="none" stroke="#d71f26" stroke-width="1.6"/></svg>Micro – Breweries</li>
          <li><svg width="9" height="8" viewBox="0 0 9 8"><path d="M1 4 L3.5 6.5 L8 1" fill="none" stroke="#d71f26" stroke-width="1.6"/></svg>Bars &amp; Taverns</li>
          <li><svg width="9" height="8" viewBox="0 0 9 8"><path d="M1 4 L3.5 6.5 L8 1" fill="none" stroke="#d71f26" stroke-width="1.6"/></svg>Cafés, Bakeries &amp; Coffee Shops</li>
          <li><svg width="9" height="8" viewBox="0 0 9 8"><path d="M1 4 L3.5 6.5 L8 1" fill="none" stroke="#d71f26" stroke-width="1.6"/></svg>Hotel Restaurants &amp;<br>Banquet Halls</li>
        </ul>
        <ul class="spec-col">
          <li><svg width="9" height="8" viewBox="0 0 9 8"><path d="M1 4 L3.5 6.5 L8 1" fill="none" stroke="#d71f26" stroke-width="1.6"/></svg>Catering Companies</li>
          <li><svg width="9" height="8" viewBox="0 0 9 8"><path d="M1 4 L3.5 6.5 L8 1" fill="none" stroke="#d71f26" stroke-width="1.6"/></svg>Food Trucks &amp; Mobile<br>Kitchens</li>
          <li><svg width="9" height="8" viewBox="0 0 9 8"><path d="M1 4 L3.5 6.5 L8 1" fill="none" stroke="#d71f26" stroke-width="1.6"/></svg>Pizzerias, Delivery &amp; Takeout</li>
          <li><svg width="9" height="8" viewBox="0 0 9 8"><path d="M1 4 L3.5 6.5 L8 1" fill="none" stroke="#d71f26" stroke-width="1.6"/></svg>Wineries &amp; Tasting Rooms</li>
          <li><svg width="9" height="8" viewBox="0 0 9 8"><path d="M1 4 L3.5 6.5 L8 1" fill="none" stroke="#d71f26" stroke-width="1.6"/></svg>Multi-Location Groups &amp;<br>Franchise Owners</li>
          <li><svg width="9" height="8" viewBox="0 0 9 8"><path d="M1 4 L3.5 6.5 L8 1" fill="none" stroke="#d71f26" stroke-width="1.6"/></svg>Commercial Kitchens &amp; Ghost<br>Kitchens</li>
        </ul>
        <ul class="spec-col">
          <li><svg width="9" height="8" viewBox="0 0 9 8"><path d="M1 4 L3.5 6.5 L8 1" fill="none" stroke="#d71f26" stroke-width="1.6"/></svg>New Openings &amp; Build-Outs</li>
          <li><svg width="9" height="8" viewBox="0 0 9 8"><path d="M1 4 L3.5 6.5 L8 1" fill="none" stroke="#d71f26" stroke-width="1.6"/></svg>Small &amp; Start-Up<br>Restaurants</li>
          <li><svg width="9" height="8" viewBox="0 0 9 8"><path d="M1 4 L3.5 6.5 L8 1" fill="none" stroke="#d71f26" stroke-width="1.6"/></svg>Restaurant Building<br>Owners &amp; Lessors</li>
          <li><svg width="9" height="8" viewBox="0 0 9 8"><path d="M1 4 L3.5 6.5 L8 1" fill="none" stroke="#d71f26" stroke-width="1.6"/></svg>Event &amp; Private Dining Venues</li>
          <li><svg width="9" height="8" viewBox="0 0 9 8"><path d="M1 4 L3.5 6.5 L8 1" fill="none" stroke="#d71f26" stroke-width="1.6"/></svg>Package Stores</li>
          <li><svg width="9" height="8" viewBox="0 0 9 8"><path d="M1 4 L3.5 6.5 L8 1" fill="none" stroke="#d71f26" stroke-width="1.6"/></svg>POS &amp; Online Ordering Risks</li>
          <li><svg width="9" height="8" viewBox="0 0 9 8"><path d="M1 4 L3.5 6.5 L8 1" fill="none" stroke="#d71f26" stroke-width="1.6"/></svg>Owner Personal Risks</li>
        </ul>
      </div>
    </div>

    <div class="abs policies">
      <h2 class="section-title serif">Personal Insurance Policies</h2>
      <p><b>Kovalen Brokerage's</b> goal is to protect the owner behind the restaurant too. Your family and personal assets deserve the right coverage at an affordable rate. Whether you need auto, home, or any other personal coverage, we tailor one package that fits your business and your life.</p>
      <div class="policy-grid">
        <div class="policy"><span class="policy-icon"><svg width="20" height="12" viewBox="0 0 20 12"><path d="M2 8 L4 3 H15 L18 8 Z M1 8 H19 V10 H1 Z" fill="none" stroke="#333" stroke-width="1.2"/><circle cx="5" cy="10.5" r="1.3" fill="#333"/><circle cx="15" cy="10.5" r="1.3" fill="#333"/></svg></span>AUTO &amp; MOTOR<br>VEHICLE INSURANCE</div>
        <div class="policy"><span class="policy-icon"><svg width="16" height="16" viewBox="0 0 16 16"><path d="M3 14 V7 L8 3 L13 7 V14 Z M6 14 V10 H10 V14" fill="none" stroke="#333" stroke-width="1.2"/></svg></span>BUILDERS<br>RISK</div>
        <div class="policy"><span class="policy-icon"><svg width="16" height="16" viewBox="0 0 16 16"><path d="M1 8 L8 2 L15 8 M3 7 V14 H13 V7" fill="none" stroke="#333" stroke-width="1.2"/></svg></span>HOME &amp; PROPERTY<br>OWNER INSURANCE</div>
        <div class="policy"><span class="policy-icon"><svg width="20" height="12" viewBox="0 0 20 12"><path d="M1 7 H19 L16 11 H4 Z M7 7 V2 H13 L15 7" fill="none" stroke="#333" stroke-width="1.2"/></svg></span>RV, BOAT,<br>MOTORCYCLE, PWC</div>
        <div class="policy"><span class="policy-icon"><svg width="16" height="16" viewBox="0 0 16 16"><path d="M2 14 V6 L8 2 L14 6 V14 Z M5 14 V9 M8 14 V7 M11 14 V10" fill="none" stroke="#333" stroke-width="1.2"/></svg></span>INVESTMENT<br>PROPERTY INSURANCE</div>
        <div class="policy"><span class="policy-icon"><svg width="16" height="14" viewBox="0 0 16 14"><path d="M1 5 L4 1 H12 L15 5 L8 13 Z M1 5 H15" fill="none" stroke="#333" stroke-width="1.2"/></svg></span>JEWELRY</div>
      </div>
    </div>
    <div class="abs policies-photo" role="img" aria-label="Photo of a smiling restaurant-owning couple reviewing their policy with an advisor"></div>

    <div class="abs coverages-frame">
      <div class="coverages">
        <h2 class="serif">Coverages</h2><span class="rule"></span>
        <div class="cov-cols">
          <ul><li>General Liability</li><li>FF&amp;E (Furniture, Fixtures,<br>and Equipment) Property</li><li>Workers Compensation</li><li>Umbrella</li></ul>
          <ul><li>Auto</li><li>Cyber</li><li>EPLI</li><li>Bonds</li><li>Liquor Liability</li></ul>
        </div>
      </div>
    </div>

    <div class="abs carriers">
      <h2 class="section-title serif">Carriers</h2><span class="rule"></span>
      <div class="carrier-grid">
        <div class="carrier"><i></i>The Wexmoor</div>
        <div class="carrier"><i></i>Bastion</div>
        <div class="carrier"><i></i>Ferrow Common</div>
        <div class="carrier"><i></i>Wayfarers</div>
        <div class="carrier"><i></i>Plains Motor</div>
        <div class="carrier"><i></i>CountyFirst</div>
        <div class="carrier"><i></i>DELVA</div>
        <div class="carrier"><i></i>Quorra</div>
        <div class="carrier"><i></i>Holloway</div>
        <div class="carrier"><i></i>KTO</div>
      </div>
    </div>

    <div class="abs why">
      <h2 class="section-title serif">Why Choose Independent</h2>
      <p><b>Kovalen Brokerage</b> is an independently owned boutique risk management group with locations at beautiful Lake Ardell in Millbrook, Georgia and Downtown Fenwick, Georgia. We know the restaurant business – tight margins, long hours, liquor laws, staff turnover and equipment that cannot fail on a Friday night. Our charge is to provide business, personal and life insurance services and risk management plans at competitive prices with truly personal service. As an independent agency, we are driven by our clients, matching each restaurant with the best possible coverage for its needs, regardless of the carrier. That flexibility lets us work with a wide variety of carriers, so owners and CFOs always get the right coverage at the right price.</p>
    </div>

    <footer class="abs footer">
      <div class="footer-addr">
        <div class="place">LAKE ARDELL</div>
        <div>480 Harbor Point Lane, Suite 12, Millbrook, GA 30000</div>
        <div class="footer-phone"><svg width="10" height="12" viewBox="0 0 10 12"><path d="M2 0.5 L4 3.5 L3 4.8 Q4.3 7.6 6.4 8.9 L7.6 8 L9.8 10.2 L8.4 11.5 Q1.6 9.8 0.4 2 Z" fill="#d71f26"/></svg>(555) 014-2270</div>
      </div>
      <span class="footer-div"></span>
      <div class="footer-web">
        <div><svg width="10" height="10" viewBox="0 0 10 10"><circle cx="5" cy="5" r="4.3" fill="none" stroke="#d71f26" stroke-width="1.2"/><path d="M0.7 5H9.3M5 0.7Q2.4 5 5 9.3M5 0.7Q7.6 5 5 9.3" fill="none" stroke="#d71f26" stroke-width="0.9"/></svg>www.kovalenbrokerage.example</div>
        <div><svg width="11" height="8" viewBox="0 0 11 8"><rect x="0.5" y="0.5" width="10" height="7" fill="none" stroke="#d71f26"/><path d="M0.5 0.5 L5.5 4.5 L10.5 0.5" fill="none" stroke="#d71f26"/></svg>info@kovalenbrokerage.example</div>
      </div>
      <div class="footer-logo"><i></i>Kovalen</div>
    </footer>
  </section>

</main>
</body>
</html>
```